Newlyweds banner image for wedding reception

Banner with the words “The Newlyweds” (No quotations) in an elegant and thick (bold) font. Font must be easy to read. Gold or silver letters. Words should easily be edited so that we have the option to print in gold or silver. No background. Image must have source file as well as be delivered as a png with a transparent background. Image will be printed in a horizontal orientation. Must be 300 Dpi for printing. Image must not lose any quality and remain crisp and sharp when expanded and printed to a size of up to 6 feet wide and 2 feet tall. Be creative but we are looking for an elegant option. First and foremost.

Target Market(s)

Wedding planners, brides planning wedding and reception

Industry/Entity Type

Wedding decoration

Colors

Designer to choose colors to be used in the design.

Requirements
Must have
• Gold or Silver letters
Should not have
• Do not mix colors

```html
<!DOCTYPE html>
<html lang="en">
<head>
<meta charset="utf-8">
<title>The Newlyweds – Reception Banner</title>
<link rel="stylesheet" href="https://fonts.googleapis.com/css2?family=Playfair+Display:wght@800&display=swap">
<style>
  :root {
    --page-bg: #f2f2f2;
    --navy-center: #062749;
    --navy-edge: #031a31;
    --gold-light: #fff3a8;
    --gold-mid: #e3b83a;
    --gold-deep: #a8741a;
    --shadow: rgba(0, 0, 0, 0.35);
  }
  html, body {
    margin: 0;
    padding: 0;
    width: 1062px;
    height: 1200px;
    overflow: hidden;
    background: var(--page-bg);
  }
  .canvas {
    position: relative;
    width: 1062px;
    height: 1200px;
  }
  .banner {
    position: absolute;
    left: 31px;
    top: 433px;
    width: 1000px;
    height: 333px;
    box-shadow: 0 14px 26px var(--shadow);
  }
  .banner svg {
    display: block;
    width: 100%;
    height: 100%;
  }
  .banner-title {
    font-family: "Playfair Display", Georgia, serif;
    font-weight: 800;
    font-size: 84px;
  }
</style>
</head>
<body>
<main class="canvas">
  <section class="banner">
    <svg viewBox="0 0 1000 333" xmlns="http://www.w3.org/2000/svg">
      <defs>
        <radialGradient id="navy-field" cx="50%" cy="40%" r="70%">
          <stop offset="0" stop-color="var(--navy-center)"/>
          <stop offset="1" stop-color="var(--navy-edge)"/>
        </radialGradient>
        <linearGradient id="gold-foil" x1="0" y1="0" x2="0" y2="1">
          <stop offset="0" stop-color="var(--gold-mid)"/>
          <stop offset="0.45" stop-color="var(--gold-light)"/>
          <stop offset="1" stop-color="var(--gold-deep)"/>
        </linearGradient>
        <linearGradient id="gold-line" x1="0" y1="0" x2="1" y2="0">
          <stop offset="0" stop-color="var(--gold-deep)"/>
          <stop offset="0.5" stop-color="var(--gold-light)"/>
          <stop offset="1" stop-color="var(--gold-mid)"/>
        </linearGradient>
      </defs>

      <rect class="banner-field" width="1000" height="333" fill="url(#navy-field)"/>

      <g class="banner-frame" fill="none" stroke="url(#gold-line)" stroke-width="1.6">
        <rect x="36" y="36" width="880" height="260"/>
        <rect x="42" y="42" width="868" height="248"/>
      </g>

      <g role="img" aria-label="Gold leaf spray ornament">
        <rect x="14" y="10" width="159" height="105" rx="40" fill="url(#gold-foil)" opacity="0.55"/>
      </g>
      <g role="img" aria-label="Small gold berry sprig ornament">
        <rect x="53" y="239" width="101" height="62" rx="28" fill="url(#gold-foil)" opacity="0.45"/>
      </g>
      <g role="img" aria-label="Gold flourish swirl ornament">
        <rect x="853" y="33" width="109" height="265" rx="48" fill="url(#gold-foil)" opacity="0.55"/>
      </g>

      <text class="banner-title" x="70" y="197" textLength="756" lengthAdjust="spacingAndGlyphs" fill="url(#gold-foil)">THE NEWLYWEDS</text>
    </svg>
  </section>
</main>
</body>
</html>
```